Supplement Bottle Label Design and Creative Lifestyle Images

We are a medical home consumer brand and we are releasing a supplement line of products called "Velbrook Nutrition". We are in need of a supplement bottle design for our supplement line, Velbrook Nutrition. We are looking for a very appealing, simple, and clean design, but with a medical feel to it.

We would like to see designs with a black background as well as designs with a white background. Bottle size will approximately be 200cc and label will about be 7" x 2.5", but this size is subject to change.

We really like the Pirlen Nutrition design and the Gantry Lab, however, we like the medical style of Nutrition Keystones. Please reference the links below.

To start off, the title of this bottle will be "Calm-Spire". We will need all similar warning about FDA, made in USA, non-GMA, GMP, ect. Please use the formula below to start:

2 Pills per serving
Blueberry pterostilbene - 10mg
Bacopa - 150mg
Gingko Biloba - 50mg
Vinpocetine - 10mg
Alpha-GPC -150mg
TAU - 35mg

https://www.shopvarn.example/Pirlen-Nutrition/b/ref=bl_dp_s_web_48213907562?ie=UTF8&node=48213907562&field-lbr_brands_browse-bin=Pirlen+Nutrition

https://www.shopvarn.example/l/7394208156

https://www.shopvarn.example/Nutrition-Keystones/b/ref=bl_dp_s_web_86420531977?ie=UTF8&node=86420531977&field-lbr_brands_browse-bin=Nutrition+Keystones

Industry/Entity Type

Medical

```html
<!DOCTYPE html>
<html lang="en">
<head>
<meta charset="utf-8">
<title>Velbrook Nutrition – Supplement Label</title>
<link rel="stylesheet" href="https://fonts.googleapis.com/css2?family=Crimson+Text:wght@400;600;700&display=swap">
<style>
  :root {
    --page: #ffffff;
    --label: #ecebe8;
    --ink: #4f4330;
    --ink-soft: #6d6250;
    --olive: #6e5c3b;
    --gold: #c8bd93;
    --gold-line: #b9ac7c;
    --rule: #8d8574;
    --white: #ffffff;
  }
  * { box-sizing: border-box; margin: 0; padding: 0; }
  html, body {
    width: 1200px; height: 900px; overflow: hidden;
    background: var(--page);
    font-family: "Crimson Text", Georgia, serif;
    color: var(--ink);
  }
  .label {
    position: absolute; left: 40px; top: 250px;
    width: 1120px; height: 400px;
    background: var(--label);
    display: grid; grid-template-columns: 373px 374px 373px;
    box-shadow: 0 2px 10px rgba(0,0,0,.12);
  }
  .panel { position: relative; padding: 22px 22px; }
  .panel + .panel { border-left: 1px dashed #d2cfc8; }

  /* left panel */
  .use-title { font-size: 20px; font-weight: 700; letter-spacing: .3px; }
  .use-text { font-size: 16px; line-height: 1.35; margin-bottom: 12px; }
  .caution {
    background: var(--olive); color: var(--white);
    padding: 8px 10px; font-size: 16px; line-height: 1.35;
    border-radius: 0 6px 6px 0; margin-left: -22px; padding-left: 22px;
  }
  .caution h3 { font-size: 18px; font-weight: 700; }
  .allergen { font-size: 15px; margin: 10px 0; color: var(--ink-soft); }
  .allergen strong { color: var(--ink); }
  .storage {
    border: 1.5px solid var(--rule); border-radius: 0 6px 6px 0;
    margin-left: -22px; padding: 6px 10px 6px 22px;
    font-size: 15px; line-height: 1.4;
  }

  /* center panel */
  .center { text-align: center; padding-top: 40px; }
  .brand { font-size: 46px; font-weight: 700; color: var(--ink); line-height: 1; }
  .brand span { display: block; font-size: 30px; margin-top: 6px; }
  .benefits { display: flex; justify-content: space-between; padding: 0 14px; margin-top: 38px; }
  .benefits svg { width: 74px; height: 84px; }
  .benefits text { font-family: "Crimson Text", Georgia, serif; font-size: 13px; fill: var(--ink-soft); letter-spacing: .5px; }
  .specs {
    display: flex; justify-content: center; margin: 26px auto 0; width: 220px;
    border-top: 2px solid var(--rule); border-bottom: 2px solid var(--rule);
    padding: 6px 0;
  }
  .specs div { flex: 1; font-size: 24px; font-weight: 700; line-height: 1; }
  .specs div + div { border-left: 2px solid var(--rule); }
  .specs small { display: block; font-size: 14px; letter-spacing: .5px; margin-top: 4px; }
  .band {
    position: absolute; left: 0; right: 0; bottom: 0; height: 40px;
    background: var(--gold); border-top: 3px solid var(--gold-line);
    font-size: 18px; font-weight: 700; letter-spacing: .6px;
    display: flex; align-items: center; justify-content: center;
  }

  /* right panel */
  .right { display: grid; grid-template-columns: 1fr 52px; gap: 12px; padding-top: 16px; }
  .facts { border: 1.5px solid var(--rule); padding: 4px 8px; }
  .facts h3 { font-size: 20px; font-weight: 700; line-height: 1.1; }
  .serving { display: flex; justify-content: space-between; font-size: 11px; color: var(--ink-soft); border-bottom: 3px solid var(--rule); padding-bottom: 3px; }
  .facts table { width: 100%; border-collapse: collapse; font-size: 11.5px; color: var(--ink-soft); }
  .facts th { font-weight: 400; text-align: right; padding: 3px 0; border-bottom: 1.5px solid var(--rule); }
  .facts td { padding: 4px 0; border-bottom: 1px solid #b8b2a4; }
  .facts td.amt { text-align: right; }
  .facts td.dv { text-align: right; width: 34px; }
  .note { font-size: 11px; color: var(--ink-soft); padding-top: 3px; }
  .other h4 { font-size: 15px; font-weight: 700; margin-top: 8px; }
  .other p { font-size: 12.5px; color: var(--ink-soft); line-height: 1.35; }
  .contact { font-size: 12.5px; color: var(--ink-soft); line-height: 1.35; margin-top: 10px; }
  .contact b { color: var(--ink); }
  .badges { display: flex; flex-direction: column; align-items: center; gap: 16px; padding-top: 6px; }
  .badge-square { width: 38px; height: 42px; border: 2px solid #222; }
  .badge-round { width: 46px; height: 46px; border-radius: 50%; background: #555; border: 3px solid #bbb; }
  .badge-flag { width: 42px; height: 30px; background: linear-gradient(#b22234 0 50%, #f2f2f2 50% 100%); }
  .badge-tested { width: 36px; height: 38px; background: #222; }
</style>
</head>
<body>
<main class="label">
  <section class="panel left">
    <h2 class="use-title">SUGGESTED USE:</h2>
    <p class="use-text">1 capsule taken 1 to 2 times daily preferably with meals or as directed by a healthcare professional.</p>
    <div class="caution">
      <h3>CAUTION:</h3>
      <p>Do not exeed recommended dose, pregnant or nursing mothers, children under 18 and individuals with a know medical condition should consult a physician before using this or any dietry supplement.</p>
    </div>
    <p class="allergen"><strong>ALLERGEN WARNING:</strong> CONTAINS SOY (LECITHIN)</p>
    <p class="storage">Keep out of reach of children, Do not use if safety seal is damaged or missing. Store in a cool, dry place.</p>
  </section>

  <section class="panel center">
    <h1 class="brand">Velbrook <span>Nutrition</span></h1>
    <div class="benefits">
      <svg viewBox="0 0 74 84" aria-label="Memory"><polygon points="37,3 71,22 71,62 37,81 3,62 3,22" fill="#e4e2dc" stroke="#c8bd93" stroke-width="3"/><text x="37" y="47" text-anchor="middle" transform="rotate(-30 37 42)">MEMORY</text></svg>
      <svg viewBox="0 0 74 84" aria-label="Focus"><polygon points="37,3 71,22 71,62 37,81 3,62 3,22" fill="#e4e2dc" stroke="#c8bd93" stroke-width="3"/><text x="37" y="47" text-anchor="middle" transform="rotate(-30 37 42)">FOCUS</text></svg>
      <svg viewBox="0 0 74 84" aria-label="Clarity"><polygon points="37,3 71,22 71,62 37,81 3,62 3,22" fill="#e4e2dc" stroke="#c8bd93" stroke-width="3"/><text x="37" y="47" text-anchor="middle" transform="rotate(-30 37 42)">CLARITY</text></svg>
    </div>
    <div class="specs">
      <div>00<small>MG</small></div>
      <div>30<small>CAPSULES</small></div>
    </div>
    <div class="band">DIETARY SUPPLEMENT</div>
  </section>

  <section class="panel right">
    <div class="info">
      <div class="facts">
        <h3>SUPPEMENTS FACTS</h3>
        <div class="serving"><span>Serving size: 2 pills</span><span>Servings per container: 30</span></div>
        <table>
          <tr><th colspan="2">Amount Per Serving</th><th>%DV</th></tr>
          <tr><td>Blueberry pterostilbene</td><td class="amt">10mg</td><td class="dv">**</td></tr>
          <tr><td>Bacopa</td><td class="amt">150mg</td><td class="dv">**</td></tr>
          <tr><td>Gingko Biloba</td><td class="amt">50mg</td><td class="dv">**</td></tr>
          <tr><td>Vinpocetine</td><td class="amt">10mg</td><td class="dv">**</td></tr>
          <tr><td>Alpha-GPC</td><td class="amt">150mg</td><td class="dv">**</td></tr>
          <tr><td>TAU</td><td class="amt">35mg</td><td class="dv">**</td></tr>
        </table>
        <p class="note">** Daily value (dv) not established.</p>
      </div>
      <div class="other">
        <h4>OTHER INGREDIENTS:</h4>
        <p>Gelatin (Capsule), Rice Flour and Vegetable Magnesium Stearate.</p>
      </div>
      <div class="contact">
        <b>Address</b><br>street, City, Country<br>
        <b>Website</b><br>www.website.com<br>email@email.com
      </div>
    </div>
    <div class="badges">
      <div class="badge-square" role="img" aria-label="Registered facility badge"></div>
      <div class="badge-round" role="img" aria-label="Non-GMO badge"></div>
      <div class="badge-flag" role="img" aria-label="Manufactured in USA flag"></div>
      <div class="badge-round" role="img" aria-label="GMP standard badge"></div>
      <div class="badge-tested" role="img" aria-label="Third party tested badge"></div>
    </div>
  </section>
</main>
</body>
</html>
```